Targeted Marketing

Postcard will be sent to customers who’ve already been contacted or will be in the next week or two reiterating information found on my website www.pinevaleminerals.example. Trying to keep my company name in the forefront of their mind when it comes time to divest their mineral interests.

```html
<!DOCTYPE html>
<html lang="en">
<head>
<meta charset="utf-8">
<title>Pinevale Minerals Postcard</title>
<link rel="stylesheet" href="https://fonts.googleapis.com/css2?family=Roboto:wght@400;700;900&family=Source+Sans+3:wght@400&display=swap">
<style>
  :root {
    --brand-red: #ed1c24;
    --deep-red: #d71920;
    --ink: #1b1b1b;
    --panel-grey: #f3f3f3;
    --paper: #ffffff;
    --backdrop: #c3ccd1;
  }
  * { margin: 0; padding: 0; box-sizing: border-box; }
  html, body { width: 893px; height: 1200px; overflow: hidden; }
  body { background: var(--backdrop); position: relative; font-family: "Roboto", sans-serif; color: var(--ink); }

  .card { position: absolute; background: var(--paper); overflow: hidden; }

  /* Front */
  .card-front { left: 30px; top: 34px; width: 830px; height: 545px; }
  .brand-lockup { position: absolute; left: 0; right: 0; top: 150px; display: flex; align-items: center; justify-content: center; gap: 22px; }
  .brand-mark { width: 46px; height: 46px; background: var(--brand-red); }
  .brand-name { font-family: "Roboto", sans-serif; font-weight: 900; font-size: 66px; letter-spacing: -1.5px; color: var(--ink); }
  .front-band { position: absolute; left: 0; top: 0; width: 830px; height: 545px; }
  .website { position: absolute; left: 0; right: 0; top: 404px; text-align: center; font-family: "Source Sans 3", sans-serif; font-size: 43px; color: var(--paper); }

  /* Back */
  .card-back { left: 32px; top: 620px; width: 830px; height: 546px; }
  .side-stripe { position: absolute; left: 18px; top: 0; width: 45px; height: 100%; background: linear-gradient(180deg, var(--brand-red), var(--deep-red)); }
  .info-panel { position: absolute; left: 63px; top: 0; width: 342px; height: 100%; background: var(--panel-grey); }
  .back-lockup { position: absolute; left: 74px; top: 30px; display: flex; align-items: center; gap: 10px; }
  .back-lockup .brand-mark { width: 22px; height: 22px; }
  .back-lockup .brand-name { font-size: 30px; letter-spacing: -0.6px; }
  .company-name { position: absolute; left: 74px; top: 116px; font-size: 21px; color: var(--brand-red); }
  .contact-row { position: absolute; left: 74px; font-size: 20.5px; line-height: 22px; color: var(--ink); }
  .contact-icon { position: absolute; left: 28px; width: 24px; height: 24px; }
  .stamp-box { position: absolute; left: 667px; top: 29px; width: 130px; height: 142px; border: 1.3px solid var(--ink); }
  .address-line { position: absolute; left: 435px; width: 363px; height: 2px; background: var(--ink); }
</style>
</head>
<body>

<section class="card card-front">
  <svg class="front-band" viewBox="0 0 830 545" aria-hidden="true">
    <polygon points="0,312 374,312 410,344 442,312 830,312 830,545 0,545" fill="var(--brand-red)"/>
  </svg>
  <div class="brand-lockup">
    <span class="brand-mark"></span>
    <span class="brand-name">Pinevale Minerals</span>
  </div>
  <p class="website">www.pinevaleminerals.example</p>
</section>

<section class="card card-back">
  <div class="side-stripe"></div>
  <div class="info-panel"></div>

  <div class="back-lockup">
    <span class="brand-mark"></span>
    <span class="brand-name">Pinevale Minerals</span>
  </div>

  <p class="company-name">Pinevale Minerals LLC</p>

  <svg class="contact-icon" style="top:156px" viewBox="0 0 24 24" fill="none" stroke="#fff" stroke-width="1.5" aria-hidden="true">
    <path d="M12 15s-5-5-5-8.5a5 5 0 0 1 10 0C17 10 12 15 12 15z"/><circle cx="12" cy="6.5" r="1.8"/>
    <path d="M3 22l3-6h12l3 6z"/>
  </svg>
  <p class="contact-row" style="top:155px">PO Box 4410<br>Dalton Springs, NM 88004</p>

  <svg class="contact-icon" style="top:207px" viewBox="0 0 24 24" fill="none" stroke="#fff" stroke-width="1.6" aria-hidden="true">
    <path d="M6 3l3 4-2 2c1 3 3 5 6 6l2-2 4 3-2 3C10 19 5 14 4 5z"/>
    <path d="M14 4a6 6 0 0 1 6 6M14 7.5a3 3 0 0 1 3 3"/>
  </svg>
  <p class="contact-row" style="top:207px">555.014.2290</p>

  <svg class="contact-icon" style="top:247px" viewBox="0 0 24 24" fill="none" stroke="#fff" stroke-width="1.5" aria-hidden="true">
    <path d="M3 10l9-6 9 6v11H3z"/><path d="M3 10l9 6 9-6M3 21l7-6M21 21l-7-6"/>
  </svg>
  <p class="contact-row" style="top:248px">jordan@pinevaleminerals.example</p>

  <div class="stamp-box"></div>
  <div class="address-line" style="top:274px"></div>
  <div class="address-line" style="top:311px"></div>
  <div class="address-line" style="top:348px"></div>
  <div class="address-line" style="top:384px"></div>
</section>

</body>
</html>
```